KVT Roofing Pty Ltd

We are a high end residential Roofing company
We would like something silimar to the attached logo with the same color scheme

Target Market(s)

High end residential Builders & Architects

Industry/Entity Type

Residential

```html
<!DOCTYPE html>
<html lang="en">
<head>
<meta charset="utf-8">
<title>KVT Roofing – Business Card</title>
<link rel="stylesheet" href="https://fonts.googleapis.com/css2?family=Arimo:wght@400;700&family=Dancing+Script:wght@700&display=swap">
<style>
  :root {
    --slate: #3f4d58;
    --slate-deep: #2d3a43;
    --stage: #33424c;
    --sky: #0f9ad0;
    --paper: #ffffff;
    --ink-grey: #4a4f54;
    --soft-white: #eef1f3;
  }
  * { margin: 0; padding: 0; box-sizing: border-box; }
  html, body {
    width: 1200px; height: 900px; overflow: hidden;
    background: var(--stage);
    font-family: "Arimo", Arial, sans-serif;
  }
  .canvas {
    width: 1200px; height: 900px;
    display: flex; flex-direction: column; align-items: center; justify-content: center;
    gap: 56px;
  }
  .card {
    width: 640px; height: 366px;
    position: relative; overflow: hidden;
    box-shadow: 0 10px 28px rgba(0,0,0,0.35);
  }
  /* Front */
  .card-front {
    background: var(--slate);
    display: flex; align-items: center; justify-content: center;
  }
  .front-wordmark {
    font-weight: 700; font-size: 46px; letter-spacing: 1px;
    color: var(--soft-white);
    text-transform: uppercase;
  }
  /* Back */
  .card-back { background: var(--paper); }
  .back-top {
    position: absolute; left: 0; top: 0; right: 0; height: 216px;
  }
  .holder-name {
    position: absolute; left: 58px; top: 58px;
    font-family: "Dancing Script", cursive;
    font-size: 25px; color: var(--sky);
  }
  .holder-role {
    position: absolute; left: 58px; top: 92px;
    font-size: 14px; color: var(--ink-grey);
  }
  .brand-block {
    position: absolute; right: 64px; top: 24px;
    display: flex; flex-direction: column; align-items: center; gap: 10px;
  }
  .brand-square { width: 124px; height: 98px; background: var(--slate); }
  .brand-name {
    font-weight: 700; font-size: 15px; color: var(--slate);
    text-transform: uppercase; letter-spacing: 0.5px;
  }
  .back-band {
    position: absolute; left: 0; right: 0; bottom: 0; height: 150px;
    background: var(--slate);
  }
  .band-wordmark {
    position: absolute; left: 40px; top: 58px;
    font-weight: 700; font-size: 26px; color: var(--soft-white);
    text-transform: uppercase;
  }
  .contact {
    position: absolute; left: 274px; top: 16px;
    color: var(--paper); font-size: 14.5px; line-height: 20px;
  }
  .contact-address { margin-bottom: 10px; }
  .contact-line { display: flex; align-items: center; gap: 8px; height: 23px; }
  .contact-line svg { width: 16px; height: 16px; flex: none; }
</style>
</head>
<body>
<main class="canvas">
  <section class="card card-front" aria-label="Card front">
    <span class="front-wordmark">Tarrow Building</span>
  </section>

  <section class="card card-back" aria-label="Card back">
    <div class="back-top">
      <p class="holder-name">Corin Ashford</p>
      <p class="holder-role">General Manager</p>
      <div class="brand-block">
        <div class="brand-square"></div>
        <span class="brand-name">Tarrow Building</span>
      </div>
    </div>
    <div class="back-band">
      <span class="band-wordmark">Tarrow</span>
      <div class="contact">
        <p class="contact-address">218 Kessel Street<br>Harbour Point</p>
        <p class="contact-line">
          <svg viewBox="0 0 16 16" aria-hidden="true"><path fill="#0f9ad0" d="M2 5c0-2 2-3 6-3s6 1 6 3v1h-3V5H5v1H2zM4 7h8l2 6H2zm4 1.5a2 2 0 100 4 2 2 0 000-4z"/></svg>
          040.555.0182
        </p>
        <p class="contact-line">
          <svg viewBox="0 0 16 16" aria-hidden="true"><rect x="1" y="3" width="14" height="10" fill="#0f9ad0"/><path d="M1.5 3.5L8 9l6.5-5.5" stroke="#3f4d58" stroke-width="1.3" fill="none"/></svg>
          cashford@kvtroofing.com.au
        </p>
        <p class="contact-line">
          <svg viewBox="0 0 16 16" aria-hidden="true"><g fill="none" stroke="#0f9ad0" stroke-width="1.4"><circle cx="8" cy="8" r="6.5"/><ellipse cx="8" cy="8" rx="2.8" ry="6.5"/><path d="M1.5 8h13M2.5 4.8h11M2.5 11.2h11"/></g></svg>
          www.kvtroofing.com.au
        </p>
      </div>
    </div>
  </section>
</main>
</body>
</html>
```